Business Card for Jewelry Business

We need a new namecard design for a jewelry company based in Bangkok, Thailand. We have a new website recently and want the new namecard to reflect our new modern image. I have uploaded our old namecard to show you the information that needs to be on the namecard. Pls check our website www.qelnotrax.com for the new color scheme to help design the new namecard.

```html
<!DOCTYPE html>
<html lang="en">
<head>
<meta charset="utf-8">
<title>Lumora Crafters – Business Card</title>
<link href="https://fonts.googleapis.com/css2?family=Tinos:ital,wght@0,400;0,700;1,700&family=Montserrat:wght@400&display=swap" rel="stylesheet">
<style>
  :root {
    --bg: #bdbdbd;
    --paper: #ffffff;
    --teal: #52c4c8;
    --teal-deep: #2f8f94;
    --ink: #2b2b2b;
    --rule: #d9d2c8;
    --white: #ffffff;
  }
  * { box-sizing: border-box; margin: 0; padding: 0; }
  html, body { width: 1200px; height: 800px; overflow: hidden; background: var(--bg); }
  .stage { position: relative; width: 1200px; height: 800px; }

  .card {
    position: absolute;
    width: 560px; height: 320px;
    box-shadow: 0 10px 28px rgba(0,0,0,.25);
  }

  /* Front */
  .card-front {
    left: 50px; top: 90px;
    background: var(--paper);
    border-bottom: 4px solid var(--teal);
    font-family: "Tinos", serif;
    color: var(--ink);
  }
  .brand {
    position: absolute; right: 40px; top: 36px;
    display: flex; align-items: center; gap: 12px;
  }
  .brand-dot { width: 26px; height: 26px; border-radius: 50%; background: var(--teal); }
  .brand-name {
    font-family: "Tinos", serif; font-size: 26px; letter-spacing: 3px;
    text-transform: uppercase; color: var(--ink); font-weight: 400;
  }
  .rule { position: absolute; left: 40px; right: 40px; height: 1px; background: var(--rule); }
  .rule-top { top: 96px; }
  .rule-mid { top: 190px; }

  .person { position: absolute; left: 40px; top: 108px; }
  .person-name { font-size: 24px; font-weight: 700; font-style: italic; text-transform: uppercase; letter-spacing: .5px; }
  .person-title { font-size: 15px; margin-top: 2px; }

  .contacts { position: absolute; left: 40px; top: 160px; font-size: 13px; display: flex; flex-wrap: wrap; gap: 4px 14px; width: 480px; }
  .contacts { top: 150px; }
  .contact { display: inline-flex; align-items: center; gap: 5px; }
  .contact svg { width: 13px; height: 13px; flex: none; }

  .company { position: absolute; left: 40px; top: 204px; font-size: 14px; line-height: 1.45; }
  .company-name { font-weight: 700; font-style: italic; font-size: 16px; }

  /* Back */
  .card-back {
    left: 590px; top: 390px;
    background: var(--teal);
    font-family: "Montserrat", sans-serif;
    color: var(--white);
  }
  .back-brand {
    position: absolute; left: 0; right: 0; top: 100px;
    display: flex; justify-content: center; align-items: center; gap: 14px;
  }
  .back-brand .brand-dot { width: 40px; height: 40px; background: var(--teal-deep); }
  .back-brand .brand-name { font-size: 38px; color: var(--teal-deep); letter-spacing: 4px; }

  .socials {
    position: absolute; left: 40px; right: 40px; bottom: 34px;
    display: flex; justify-content: center; gap: 28px; font-size: 15px;
  }
  .social { display: inline-flex; align-items: center; gap: 8px; }
  .social-dot { width: 18px; height: 18px; border-radius: 50%; background: var(--white); }
</style>
</head>
<body>
<main class="stage">

  <section class="card card-front">
    <div class="brand">
      <span class="brand-dot"></span>
      <span class="brand-name">Lumora Crafters</span>
    </div>
    <div class="rule rule-top"></div>

    <div class="person">
      <p class="person-name">Nisa Tervalong</p>
      <p class="person-title">Sales &amp; Product Development Manager</p>
    </div>

    <div class="contacts">
      <span class="contact">
        <svg viewBox="0 0 16 16"><path fill="#52c4c8" d="M3 1l3 3-1.5 2a9 9 0 0 0 5.5 5.5L12 10l3 3-2 2C7 15 1 9 1 3z"/></svg>
        +662-555-0140-2
      </span>
      <span class="contact">
        <svg viewBox="0 0 16 16"><rect x="4" y="1" width="8" height="5" fill="#52c4c8"/><rect x="1" y="6" width="14" height="6" rx="1" fill="#52c4c8"/><rect x="4" y="10" width="8" height="5" fill="#fff" stroke="#52c4c8"/></svg>
        +662-555-0187
      </span>
      <span class="contact">
        <svg viewBox="0 0 16 16"><rect x="1" y="3" width="14" height="10" fill="#52c4c8"/><path d="M1 3l7 6 7-6" fill="none" stroke="#fff"/></svg>
        nisa@qelnotrax.com
      </span>
      <span class="contact">
        <svg viewBox="0 0 16 16"><rect x="1" y="3" width="14" height="10" fill="#52c4c8"/><path d="M1 3l7 6 7-6" fill="none" stroke="#fff"/></svg>
        info@qelnotrax.com
      </span>
      <span class="contact">
        <svg viewBox="0 0 16 16"><circle cx="8" cy="8" r="7" fill="none" stroke="#52c4c8" stroke-width="1.5"/><path d="M1 8h14M8 1c3 3 3 11 0 14M8 1c-3 3-3 11 0 14" fill="none" stroke="#52c4c8"/></svg>
        http://www.qelnotrax.com
      </span>
    </div>
    <div class="rule rule-mid"></div>

    <div class="company">
      <p class="company-name">Lumora Crafters Co.,Ltd</p>
      <p>128 Moo 7 Sukprasert Road, Export Processing Zone 2</p>
      <p>Bang Phli Industrial Park, Bang Phli, Bangkok 10540 Thailand</p>
    </div>
  </section>

  <section class="card card-back">
    <div class="back-brand">
      <span class="brand-dot"></span>
      <span class="brand-name">Lumora Crafters</span>
    </div>
    <div class="socials">
      <span class="social"><span class="social-dot"></span>Lumora Crafters</span>
      <span class="social"><span class="social-dot"></span>@LumoraCrafters</span>
    </div>
  </section>

</main>
</body>
</html>
```